Luggage and travel essentials company needs Letterhead design (including logo)

Brenmoor luggage is a travel retailer focussed on selling luggage and travel essentials.
We are a company that have a traditional approach to customer service and also embraces the latest technology, especially where it improves the customer experience.
I would like the design to have an airport hint (airport imagery and font preferred), I would also like the colour blue to feature heavily (see attached image for colour hint).
The final design should aim to give the customer confidence that we are dependable and reliable (no script fonts or crazy colours please) but also reflect that we are an innovative and technology focused company.
I would like the letterhead design to include a logo and text.
I am interested in letterhead text containing an embedded logo (much like the 'A' in Zyvanta's logo is also used separately) Note: this is optional.
The text of the letterhead should include the words "Brenmoor Luggage & Travel Essentials", and should include a space for the company phone number, email address, website address along with the company physical address.
Target Market(s)
Affluent Adults aged 25 years and above - Predominantly female
Industry/Entity Type
Airport

```html
<!DOCTYPE html>
<html lang="en">
<head>
<meta charset="utf-8">
<title>Brenmoor Luggage &amp; Travel Essentials – Letterhead</title>
<link rel="stylesheet" href="https://fonts.googleapis.com/css2?family=Montserrat:wght@700&family=Questrial&family=PT+Serif&display=swap">
<style>
  :root {
    --backdrop: #ecebe8;
    --paper: #ffffff;
    --brand-blue: #3a96d8;
    --brand-grey: #c6c5c7;
    --mark-grey: #8f8f93;
    --ink-dark: #4a4a4e;
    --ink-body: #55555a;
    --rule: #bdbdbd;
  }
  * { box-sizing: border-box; margin: 0; padding: 0; }
  html, body {
    width: 1200px; height: 900px; overflow: hidden;
    background: var(--backdrop);
  }
  .letterhead {
    position: absolute; left: 296px; top: 20px;
    width: 608px; height: 860px;
    background: var(--paper);
    box-shadow: 0 2px 10px rgba(0,0,0,0.12);
    overflow: hidden;
  }
  .brand-mark {
    position: absolute; left: 66px; top: 56px;
    width: 62px; height: 62px; border-radius: 50%;
    background: var(--mark-grey);
  }
  .brand-name {
    position: absolute; left: 10px; top: 140px; width: 180px;
    font-family: "Montserrat", sans-serif; font-weight: 700;
    font-size: 14.5px; line-height: 17px; letter-spacing: 0.2px;
    text-transform: uppercase; text-align: center;
    color: var(--ink-dark);
  }
  .band-blue {
    position: absolute; left: 0; top: 190px; width: 171px; height: 22px;
    background: var(--brand-blue);
  }
  .band-grey {
    position: absolute; left: 190px; top: 190px; width: 70px; height: 27px;
    background: var(--brand-grey);
  }
  .column-rule {
    position: absolute; left: 185px; top: 212px; width: 3px; height: 636px;
    background: var(--brand-blue);
  }
  .contact-list {
    position: absolute; left: 0; top: 250px; width: 185px;
    list-style: none;
    font-family: "Questrial", sans-serif; font-size: 11.5px; line-height: 15px;
    color: var(--ink-dark); text-align: center;
  }
  .contact-item { position: absolute; left: 0; width: 185px; }
  .contact-item svg { display: block; margin: 0 auto 10px; }
  .contact-item--address { top: 0; }
  .contact-item--email { top: 163px; }
  .contact-item--phone { top: 313px; }
  .contact-item--web { top: 451px; }
  .contact-divider {
    position: absolute; left: 38px; width: 110px; height: 1px;
    background: var(--rule);
  }
  .letter {
    position: absolute; left: 210px; top: 268px; width: 336px;
    font-family: "PT Serif", serif; font-size: 8px; line-height: 12.5px;
    color: var(--ink-body); text-align: justify;
  }
  .letter-heading { margin-bottom: 46px; line-height: 11px; }
  .letter p + p { margin-top: 12px; }
  .footer-grey {
    position: absolute; left: 0; bottom: 0; width: 171px; height: 12px;
    background: var(--brand-grey);
  }
  .footer-blue {
    position: absolute; left: 198px; bottom: 0; width: 410px; height: 12px;
    background: var(--brand-blue);
  }
</style>
</head>
<body>
<main class="letterhead">
  <div class="brand-mark" aria-hidden="true"></div>
  <h1 class="brand-name">Brenmoor Luggage &amp;<br>Travel Essentials</h1>

  <div class="band-blue"></div>
  <div class="band-grey"></div>
  <div class="column-rule"></div>

  <ul class="contact-list">
    <li class="contact-item contact-item--address">
      <svg width="16" height="22" viewBox="0 0 16 22" aria-hidden="true">
        <path d="M8 1a7 7 0 0 0-7 7c0 5 7 13 7 13s7-8 7-13a7 7 0 0 0-7-7z" fill="none" stroke="var(--brand-blue)" stroke-width="2"/>
        <circle cx="8" cy="8" r="2.5" fill="var(--brand-blue)"/>
      </svg>
      14, Mill Lane,<br>Redbrook, Kent,<br>TN9 4QX
    </li>
    <li class="contact-divider" style="top:118px"></li>
    <li class="contact-item contact-item--email">
      <svg width="24" height="16" viewBox="0 0 24 16" aria-hidden="true">
        <rect x="0" y="0" width="24" height="16" rx="1" fill="var(--brand-blue)"/>
        <path d="M1 1l11 8 11-8M1 15l8-7M23 15l-8-7" fill="none" stroke="#fff" stroke-width="1.3"/>
      </svg>
      info@brenmoorluggage.co.uk
    </li>
    <li class="contact-divider" style="top:273px"></li>
    <li class="contact-item contact-item--phone">
      <svg width="26" height="20" viewBox="0 0 26 20" aria-hidden="true">
        <path d="M2 7c0-4 22-4 22 0v2h-6V6H8v3H2z" fill="var(--brand-blue)"/>
        <path d="M6 9h14l3 10H3z" fill="var(--brand-blue)"/>
        <circle cx="13" cy="14" r="3" fill="#fff"/>
      </svg>
      01632 xxxxxx
    </li>
    <li class="contact-divider" style="top:426px"></li>
    <li class="contact-item contact-item--web">
      <svg width="18" height="18" viewBox="0 0 18 18" aria-hidden="true">
        <g fill="none" stroke="var(--brand-blue)" stroke-width="1.6">
          <circle cx="9" cy="9" r="8"/>
          <ellipse cx="9" cy="9" rx="3.5" ry="8"/>
          <path d="M1 9h16M2.5 4.5h13M2.5 13.5h13"/>
        </g>
      </svg>
      www.brenmoorluggage.co.uk
    </li>
  </ul>

  <article class="letter">
    <p class="letter-heading">Lorem ipsum<br>September 2016</p>
    <p>Thank you for choosing our store for your travel needs. We stock a careful range of cases, bags and accessories for every journey, from short city breaks to long haul trips abroad. Our team is always ready to help you find the right fit.</p>
    <p>Every item we sell is chosen for strength, comfort and style. We test wheels, handles and zips so that your luggage stays reliable through busy terminals and crowded carousels, season after season.</p>
    <p>Members can now reserve items online and collect them at the store before departure, saving time on the day you fly.</p>
    <p>Our new app tracks orders and sends a reminder when your bags are packed and waiting for you at the counter.</p>
    <p>We also offer repairs, name tags, travel adapters, neck pillows and a wide choice of toiletry bags. If anything is missing from your list, simply ask and we will do our best to source it for you quickly. We look forward to welcoming you again soon.</p>
  </article>

  <div class="footer-grey"></div>
  <div class="footer-blue"></div>
</main>
</body>
</html>
```